E-Commerce Website Update for Bamboo Poles Company

Existing website at:

http://www.reedcraftstudio.example/
http://www.reedcraftstudio.example/pages/product-and-price-list

Two pages to design: home page and "price list" page.

Info for home page as follows:

HOME PAGE:

Header:
Company Name: willow harmonics
Telephone: 1 888 412 3906

Across the top:
Home | Price List | Blog | FAQ | About | Contact

Down the side:
About Bamboo
Wedding Arbors
Bamboo For Flutes
Black Bamboo
Spotted Bamboo
Bamboo Carpentry
Photo Gallery
All Products & Prices
Blog
FAQ
About
Contact

Should have shopping cart and search buttons on top.
Please see ai file, attached for logo (leaf) and font
In addition the homepage should have one or two sections for promotions

Chosen design will be asked to help deign a PRODUCT AND PRICE LIST page similar to the one we have now, but with "LEARN MORE" and "ORDER NOW" buttons for each item.
Updates

Project Deadline Extended
Reason: Thanks  for all the designs so far; giving an extra week for extra consideration.

Target Market(s)

Consumers, wedding planners.

Industry/Entity Type

Shopping

Requirements
Must have
• Clean, easy to read design.
Should not have
• No flash animation.

```html
<!DOCTYPE html>
<html lang="en">
<head>
<meta charset="utf-8">
<title>willow harmonics — Bamboo Poles</title>
<link rel="stylesheet" href="https://fonts.googleapis.com/css2?family=PT+Sans:wght@400;700&family=PT+Serif&display=swap">
<style>
:root{
  --bg:#000;
  --gold:#b8892a;
  --gold-light:#d7a53a;
  --gold-text:#c9962f;
  --red:#c50d0d;
  --red-dark:#8e0505;
  --green:#3fae24;
  --footer:#222;
  --text:#fff;
  --line:#9a9a9a;
}
*{box-sizing:border-box;margin:0;padding:0}
html,body{width:1200px;height:1193px;overflow:hidden;background:var(--bg);font-family:"PT Sans",sans-serif;color:var(--text)}
.page{position:relative;width:1200px;height:1193px}
.abs{position:absolute;white-space:nowrap}

/* header */
.hero{left:113px;top:0;width:971px;height:330px;border-radius:0 0 6px 6px;
  background:linear-gradient(180deg,#6f8f3a 0%,#8fae58 30%,#7b9a4a 60%,#6b6a48 85%,#a99a6a 100%)}
.hero-reflect{left:113px;top:332px;width:971px;height:45px;
  background:linear-gradient(180deg,rgba(140,130,90,.55),rgba(0,0,0,0))}
.brand{left:113px;top:0;width:252px;height:80px;background:rgba(255,255,255,.15);
  display:flex;align-items:center;gap:10px;padding-left:10px}
.brand-mark{width:12px;height:12px;border-radius:50%;background:#fff;flex:none}
.brand-name{font-size:28px;color:#fff;line-height:1}
.cartbar{left:700px;top:0;width:384px;height:28px;background:rgba(120,90,30,.85);display:flex;align-items:center;padding-left:16px;font-size:13px}
.cartbar b{margin-right:4px}
.btn{display:inline-flex;align-items:center;justify-content:center;background:linear-gradient(#e01818,var(--red-dark));color:#fff;border-radius:4px;font-size:11px}
.cartbar .btn{width:81px;height:20px;position:absolute;top:4px}
.navbar{left:355px;top:28px;width:729px;height:36px;background:var(--gold);border-radius:18px 0 0 18px;display:flex;align-items:center;padding-left:30px}
.navbar a{color:#fff;text-decoration:none;font-variant:small-caps;font-size:15px;padding:0 15px;border-right:1px solid rgba(255,255,255,.35);line-height:18px}
.navbar a:last-of-type{border:0}
.search{left:892px;top:36px;width:186px;height:22px;background:#fff;border-radius:10px;overflow:hidden}
.search-icon{position:absolute;left:0;top:0;width:33px;height:22px;background:var(--gold-light)}
.panel{background:rgba(255,255,255,.2);border:1px solid rgba(255,255,255,.5);border-radius:6px}
.panel-left{left:113px;top:135px;width:551px;height:172px}
.panel-right{left:700px;top:64px;width:361px;height:246px;border-top:0;border-radius:0 0 6px 6px}
.hero-copy{font-size:14px;line-height:17px;color:#fff;white-space:normal}
.welcome{font-size:19px;text-align:center}
.phone{font-size:24px;text-align:center}
.gold{color:var(--gold-light)}

/* intro */
.section-title{color:var(--gold-text);font-size:18px;border-bottom:1px solid var(--line);padding-bottom:1px}
.intro p,.body-copy p{font-size:12px;line-height:14.5px}
.body-copy a{color:var(--gold-text)}
.card{width:263px;height:125px;border:2px solid var(--gold);border-radius:9px}
.card-photo{position:absolute;left:14px;top:10px;width:71px;height:104px;border:2px solid var(--gold-light)}
.card-title{position:absolute;left:110px;top:14px;font-size:12.5px}
.card-size{position:absolute;left:112px;top:36px;font-size:12.5px}
.card-actions{position:absolute;left:97px;top:87px;width:152px;height:20px;display:flex;border-radius:5px;overflow:hidden}
.card-actions span{flex:1;display:flex;align-items:center;justify-content:center;background:linear-gradient(#e01818,var(--red-dark));font-size:10px}
.card-actions span+span{border-left:1px solid #f45}
.note{font-size:10.5px;color:var(--gold-text);line-height:13px}

/* side nav */
.sidenav{left:803px;width:211px}
.sidenav li{list-style:none;height:20px;border-bottom:1px solid var(--line);font-size:12.5px;line-height:19px;padding-left:18px}
.sidenav li.active{background:var(--gold);position:relative}
.sidenav li.active:before{content:"";position:absolute;left:4px;top:5px;border-left:7px solid #fff;border-top:4px solid transparent;border-bottom:4px solid transparent}
.promo{left:776px;top:890px;width:253px;height:91px;border:1px solid #ccc;border-radius:4px;
  background:linear-gradient(160deg,#888,#444 60%,#222);text-align:center;font-family:"PT Serif",serif;font-weight:700;font-size:29px;line-height:30px;padding-top:14px;color:#fff}
.promo-reflect{left:776px;top:983px;width:253px;height:20px;background:linear-gradient(rgba(120,120,120,.5),rgba(0,0,0,0))}

/* footer */
.footer{left:0;top:1001px;width:1200px;height:192px;background:var(--footer)}
.foot-title{font-family:"PT Serif",serif;color:var(--gold-text);font-size:19px}
.contact-list{font-size:12.5px;line-height:18px}
.contact-list .lbl{color:var(--green)}
.quote{font-family:"PT Serif",serif;font-size:12px;line-height:14.5px}
.client{font-family:"PT Serif",serif;font-style:italic;color:var(--green);font-size:13px}
.foot-brand{left:855px;top:1018px;width:176px;height:44px;border-radius:22px;background:#111;display:flex;align-items:center;justify-content:center;gap:8px}
.copy{font-family:"PT Serif",serif;font-size:12px;line-height:14.5px}
.copy a{color:var(--green)}
</style>
</head>
<body>
<div class="page">

  <header>
    <div class="abs hero" role="img" aria-label="Photo of a path through a green bamboo forest with a bamboo fence"></div>
    <div class="abs hero-reflect"></div>

    <div class="abs brand"><span class="brand-mark"></span><span class="brand-name">willow<br>harmonics</span></div>

    <div class="abs cartbar"><b>SHOPPING CART:</b> 0 Items
      <span class="btn" style="left:183px">View Item</span>
      <span class="btn" style="left:274px">Checkout</span>
    </div>

    <nav class="abs navbar">
      <a href="#">Home</a><a href="#">Price List</a><a href="#">Blog</a><a href="#">FAQ</a><a href="#">About Us</a><a href="#">Contact Us</a>
    </nav>
    <div class="abs search">
      <span class="search-icon">
        <svg width="33" height="22" viewBox="0 0 33 22"><circle cx="13" cy="9" r="5" fill="none" stroke="#fff" stroke-width="2"/><line x1="17" y1="13" x2="22" y2="18" stroke="#fff" stroke-width="2.5"/></svg>
      </span>
    </div>

    <div class="abs panel panel-left"></div>
    <p class="abs hero-copy" style="left:134px;top:161px;width:250px">Need bamboo poles at a competitive price? Welcome to your one-stop pole shop.</p>
    <p class="abs hero-copy" style="left:403px;top:161px;width:250px">See our complete list of products with prices:</p>
    <span class="abs btn" style="left:170px;top:239px;width:144px;height:23px">Find Out More</span>
    <span class="abs btn" style="left:453px;top:239px;width:144px;height:23px">Clich Here</span>

    <div class="abs panel panel-right"></div>
    <p class="abs welcome" style="left:700px;top:87px;width:356px">Welcome to your Pole Provider</p>
    <p class="abs phone" style="left:695px;top:123px;width:356px">1 888 412 3906</p>
    <p class="abs hero-copy" style="left:700px;top:187px;width:361px;text-align:center;line-height:21px">Bamboo poles at wholesale prices direct<br>from <span class="gold">willow harmonics</span></p>
  </header>

  <main>
    <h2 class="abs section-title" style="left:113px;top:409px;width:612px;font-weight:400">A Little Introduction</h2>
    <div class="abs intro" style="left:144px;top:446px">
      <p>We warehouse a variety of types poles in a variety of diameters, from 5/8" to 5 1/2", in lengths up to 8'.<br>We have natural poles, moso (mao) timber poles, black poles spotted poles… and regular bamboo poles.<br>Whatever your project may be, from flutes to weddings to roasting a pig, we have the perfect pole for you.</p>
    </div>

    <div class="abs card" style="left:143px;top:512px">
      <div class="card-photo" role="img" aria-label="Pale natural bamboo poles" style="background:linear-gradient(90deg,#d9cfa4,#efe6c4,#cfc08a)"></div>
      <span class="card-title">Mao Bamboo Poles</span><span class="card-size">5” x 8’ feet</span>
      <div class="card-actions"><span>Learn More</span><span>Order Now</span></div>
    </div>
    <div class="abs card" style="left:451px;top:512px">
      <div class="card-photo" role="img" aria-label="Black bamboo poles on white" style="left:13px;background:linear-gradient(90deg,#fff 30%,#333 35%,#222 65%,#fff 70%)"></div>
      <span class="card-title" style="left:113px">Mao Bamboo Poles</span><span class="card-size" style="left:115px">5” x 8’ feet</span>
      <div class="card-actions"><span>Learn More</span><span>Order Now</span></div>
    </div>
    <div class="abs card" style="left:143px;top:661px">
      <div class="card-photo" role="img" aria-label="Thick yellow bamboo poles" style="left:16px;background:linear-gradient(90deg,#d8c58a,#f0e3a8,#cbb06a)"></div>
      <span class="card-title">Mao Bamboo Poles</span><span class="card-size">5” x 8’ feet</span>
      <div class="card-actions"><span>Learn More</span><span>Order Now</span></div>
    </div>
    <div class="abs card" style="left:451px;top:661px">
      <div class="card-photo" role="img" aria-label="Bamboo wedding arbor frame" style="left:10px;top:17px;width:80px;height:92px;background:linear-gradient(#f4f0e6,#ddd6c4)"></div>
      <span class="card-title" style="left:118px">Mao Bamboo Poles</span><span class="card-size" style="left:120px">5” x 8’ feet</span>
      <div class="card-actions" style="left:98px;top:90px"><span>Learn More</span><span>Order Now</span></div>
    </div>

    <p class="abs note" style="left:169px;top:796px">PLEASE NOTE: THAT PRICES ARE PER CARTON - Each carton contains 2 to 70 poles, depending on type<br>of pole. Please click on item for details.</p>

    <div class="abs body-copy" style="left:144px;top:843px">
      <p>Poles are warehoused in Westvale, and ready for immediate shipping by ParcelLine ground to all of the United<br>States. Or, if you’re in the Westvale area, you can collect your poles at our warehouse (see our FAQs).</p>
      <p style="margin-top:14px">Take advantage of our online shop for easy ordering. If you have any questions, contact us by calling us<br>anytime at 1.888.412.3906 or email us at <a href="#">nora@willowharmonics.example</a>.</p>
      <p style="margin-top:12px">If you prefer to purchase our poles through MarketHall, or want to see feedback information about our product,<br>please visit our MarketHall site <a href="#">here</a>.</p>
    </div>

    <aside>
      <h2 class="abs section-title" style="left:778px;top:409px;width:251px;font-weight:400">Navigation</h2>
      <ul class="abs sidenav" style="top:466px">
        <li class="active">About Bamboo</li><li>Bamboo Carpentry</li><li>Photo Gallery</li><li>All Products and Prices</li><li>Blog</li><li>FAQ</li><li>About Us</li><li>Contact Us</li>
      </ul>
      <ul class="abs sidenav" style="top:661px">
        <li>Wedding Arbors</li><li>Bamboo for Flutes</li><li>Hand Painted Bamboo Poles</li>
      </ul>
      <ul class="abs sidenav" style="top:742px">
        <li>Black Bamboo</li><li>Spotted Bamboo</li><li>Mao Bamboo</li><li>Reed Bamboo</li><li>Tonkin Bamboo</li><li>Nan Bamboo</li>
      </ul>
      <div class="abs promo">Promotional<br>Offer</div>
      <div class="abs promo-reflect"></div>
    </aside>
  </main>

  <footer>
    <div class="abs footer"></div>
    <h3 class="abs foot-title" style="left:148px;top:1009px;font-weight:400">Contact Us</h3>
    <div class="abs contact-list" style="left:152px;top:1035px">
      <p><span class="lbl">Office Hours</span> : 7:30 am - 7:00 pm</p>
      <p>Monday - Friday.</p>
      <p><span class="lbl">Toll Free</span> : 555-5555</p>
      <p><span class="lbl">Local</span> : 555-5555</p>
      <p><span class="lbl">Office</span>: Harbor Point, CA</p>
      <p><span class="lbl">Warehouse</span>: Millbrook, CA</p>
      <p style="margin-top:18px"><span class="lbl">Email</span> : nora@willowharmonics.example</p>
    </div>

    <h3 class="abs" style="left:491px;top:1011px;font-size:18px;font-weight:400;color:var(--gold-text)">Testimonials</h3>
    <span class="abs" style="left:487px;top:1036px;font-family:'PT Serif',serif;font-size:34px;font-weight:700">“</span>
    <p class="abs quote" style="left:491px;top:1064px">Lorem ipsum dolor sit amety. Lorem ipsum<br>dolor sit amety. Lorem ipsum dolor sit amety.<br>Lorem ipsum dolor sit amety.</p>
    <span class="abs" style="left:717px;top:1100px;font-family:'PT Serif',serif;font-size:34px;font-weight:700">”</span>
    <p class="abs client" style="left:493px;top:1124px">Client, MM/DD/YY</p>

    <div class="abs foot-brand"><span class="brand-mark" style="width:10px;height:10px"></span><span style="font-size:17px">willow harmonics</span></div>
    <p class="abs copy" style="left:834px;top:1088px">Copyright © 2001 <a href="#">willow harmonics.</a><br>All Rights Reserved. All Prices USD.</p>
  </footer>
</div>
</body>
</html>
```